Camp Thornbury Retreat Brochure

We are looking for someone to design a brochure/flyer that we can use to promote renting our camp facility. We don't have a specific size in mind, we are open to different options.

The link below has pictures that can be used (don't expect you to use all of them). It also has a PDF of the information that will need to be included in the brochure.

https://files.quillbox.example/folders/7KpR2-TmXa9LwQzB4nYcHd8-vUe3Fs6?usp=sharing

We are a Christian camp and retreat facility. You might want to check out our website to get a feel for what we do.

This brochure will be used to help us increase our rental business. Usually given to an organizational leader who is planning a retreat.

Target Market(s)

Church groups, community groups

Industry/Entity Type

Rental

Requirements
Must have
• Pictures
Information that was included
Website
Contact Information
Nice to have
• Logo
Should not have
• Cross
Clip art

```html
<!DOCTYPE html>
<html lang="en">
<head>
<meta charset="utf-8">
<title>Camp Thornbury Retreat Brochure</title>
<link rel="stylesheet" href="https://fonts.googleapis.com/css2?family=Oswald:wght@700&family=Source+Sans+3:wght@400;600&display=swap">
<style>
  :root {
    --backdrop: #dcdcdc;
    --paper: #ffffff;
    --tag-black: #141414;
    --tag-slate: #2a312c;
    --tag-text: #ffffff;
    --forest-light: #9fb88a;
    --forest-mid: #5f7d4a;
    --forest-dark: #33472a;
    --cabin-red: #a8382a;
    --wood-light: #c07a45;
    --wood-dark: #6b3a1e;
    --panel-green: rgba(178, 196, 160, 0.82);
    --panel-white: rgba(236, 238, 232, 0.86);
    --panel-wood: rgba(196, 160, 132, 0.8);
  }
  * { box-sizing: border-box; margin: 0; padding: 0; }
  html, body {
    width: 1200px; height: 900px; overflow: hidden;
    background: var(--backdrop);
    font-family: "Source Sans 3", sans-serif;
  }
  .spread {
    position: absolute; left: 82px; top: 50px;
    width: 1036px; height: 800px;
    display: flex;
  }
  .page {
    position: relative; width: 518px; height: 800px;
    background: var(--paper); overflow: hidden;
  }
  .photo { position: absolute; left: 0; width: 100%; }
  .section-title {
    position: absolute; left: 0; width: 100%;
    text-align: center;
    font-family: "Oswald", sans-serif; font-weight: 700;
    font-size: 58px; line-height: 1; color: #fff;
    transform: scaleY(1.12);
    text-shadow: 2px 3px 6px rgba(0,0,0,0.55);
    letter-spacing: 0.5px;
  }
  .panel { position: absolute; left: 0; width: 100%; }
  .tag {
    position: absolute; height: 24px;
    display: flex; flex-direction: column; align-items: center; justify-content: center;
    color: var(--tag-text); font-size: 15px; line-height: 1;
    white-space: nowrap;
  }
  .tag small { font-size: 8px; line-height: 1; }
  .tag .aside { font-size: 8px; margin-left: 4px; }
  .tag .row { display: flex; align-items: baseline; }
  .facilities .tag { background: var(--tag-black); height: 23px; }
  .activities .tag, .events .tag { background: var(--tag-slate); }

  /* facilities page */
  .photo-cabins { top: 0; height: 364px;
    background: linear-gradient(180deg, #d9e3cf 0%, var(--forest-mid) 35%, var(--forest-dark) 65%, var(--cabin-red) 82%, #b7a88e 100%); }
  .facilities-panel { top: 364px; height: 172px; background: var(--panel-green); }
  .photo-bunks { position: absolute; left: 350px; top: 365px; width: 160px; height: 192px;
    border: 4px solid var(--paper);
    background: linear-gradient(180deg, var(--wood-light) 0%, #8a5a34 60%, #d8d2c6 100%); }
  .photo-lodge { top: 536px; height: 264px;
    background: linear-gradient(180deg, var(--forest-light) 0%, var(--forest-mid) 40%, #9c7a56 70%, #c9c2a8 100%); }

  /* activities & events page */
  .photo-pavilion { top: 0; height: 296px;
    background: linear-gradient(180deg, #e3ead8 0%, var(--forest-mid) 35%, #b9b7ad 55%, #8d4a2b 75%, #cfc8b4 100%); }
  .activities-panel { top: 296px; height: 185px; background: var(--panel-white); }
  .photo-hall { top: 481px; height: 319px;
    background: linear-gradient(180deg, var(--wood-dark) 0%, var(--wood-light) 45%, #8a5430 70%, #a88468 100%); }
  .events-panel { top: 700px; height: 100px; background: var(--panel-wood); }
</style>
</head>
<body>
<main class="spread">
  <section class="page facilities">
    <div class="photo photo-cabins" role="img" aria-label="Red camp cabins among tall pine and oak trees"></div>
    <h2 class="section-title" style="top:100px">FACILITIES</h2>

    <div class="panel facilities-panel"></div>
    <div class="tag" style="left:19px;top:380px;width:153px"><span class="row">26 Cabins<span class="aside">(sleep 10-12)</span></span></div>
    <div class="tag" style="left:19px;top:407px;width:153px">Commercial Kitchen</div>
    <div class="tag" style="left:19px;top:435px;width:153px"><span class="row">Dining Hall<span class="aside">(seats 150)</span></span></div>
    <div class="tag" style="left:19px;top:465px;width:153px">3 Pavilions</div>
    <div class="tag" style="left:19px;top:492px;width:153px">Covered Gym<small>(with lights)</small></div>
    <div class="tag" style="left:184px;top:380px;width:148px">Pool</div>
    <div class="tag" style="left:184px;top:407px;width:148px">Recreational Lake</div>
    <div class="tag" style="left:184px;top:435px;width:148px">Sand Volleyball Pit<small>(with lights)</small></div>
    <div class="tag" style="left:184px;top:465px;width:148px">Softball Field<small>(with lights)</small></div>
    <div class="tag" style="left:184px;top:492px;width:148px">Campfire Pit</div>

    <div class="photo photo-lodge" role="img" aria-label="Stone lodge building surrounded by green trees"></div>
    <div class="photo-bunks" role="img" aria-label="Cabin interior with wooden bunk beds"></div>
  </section>

  <section class="page activities events">
    <div class="photo photo-pavilion" role="img" aria-label="Large open-sided covered pavilion under trees"></div>
    <h2 class="section-title" style="top:62px">ACTIVITIES</h2>

    <div class="panel activities-panel"></div>
    <div class="tag" style="left:38px;top:321px;width:137px">Horseback Riding</div>
    <div class="tag" style="left:38px;top:350px;width:137px">Low Ropes Course</div>
    <div class="tag" style="left:38px;top:379px;width:137px">Hatchet Throwing</div>
    <div class="tag" style="left:38px;top:408px;width:137px">Archery Tag</div>
    <div class="tag" style="left:193px;top:321px;width:137px">Fishing</div>
    <div class="tag" style="left:193px;top:350px;width:137px">Volleyball</div>
    <div class="tag" style="left:193px;top:379px;width:137px">Softball</div>
    <div class="tag" style="left:193px;top:408px;width:137px">Gaga Ball</div>
    <div class="tag" style="left:193px;top:437px;width:137px;font-size:13px">9 Sqaure-in-the-Air</div>
    <div class="tag" style="left:347px;top:321px;width:137px">Basketball</div>
    <div class="tag" style="left:347px;top:350px;width:137px">Swimming<small>(seasonal)</small></div>
    <div class="tag" style="left:347px;top:379px;width:137px">Hiking</div>
    <div class="tag" style="left:347px;top:408px;width:137px">Soccer</div>

    <div class="photo photo-hall" role="img" aria-label="Event hall with exposed wooden beams and chandeliers"></div>
    <h2 class="section-title" style="top:547px">EVENTS</h2>
    <div class="panel events-panel"></div>
    <div class="tag" style="left:19px;top:723px;width:150px">Church Retreats</div>
    <div class="tag" style="left:185px;top:723px;width:152px">Boy &amp; Girl Scouts</div>
    <div class="tag" style="left:353px;top:723px;width:151px">Weddings</div>
    <div class="tag" style="left:19px;top:754px;width:150px;font-size:12px">Organizational Meetings</div>
    <div class="tag" style="left:185px;top:754px;width:152px">School Groups</div>
  </section>
</main>
</body>
</html>
```